Pin Oak Media Outdoor Advertising Corporate Stationery Design

We need a full corporate stationary design for our company Pin Oak Media. We setup and lease billboards, building wraps, trailer ads and construction hoardings.

We need to establish our branding and our newly created logo. All our brand identity should point towards our values, vision and mission.

We are open to fresh new ideas for our stationary design as long as it ultimately reflects the brand & logo.

Corporate Stationary List:
1. Business Card Design
2. Letterhead Design
3. Email Signature Design
4. “Advertise Here” Design (for placement on empty billboards, etc)

All designs must include our logo and be kept simple, modern, friendly and effective.

All designs should please be provided in Illustrator, Photoshop and InDesign file formats.

More details are attached in Word.

Hey

The project has been guaranteed. We like what has been submitted so far but we''d like to see a few concepts for the "Advertise Here" design for open billboards please.

Thanks!

Target Market(s)

Male and female, corporates, business owners, media buying agencies, government & all age groups.

Industry/Entity Type

Construction

Requirements
Must have
• All designs must incorporate our colours: Pantone 319C, 320C, 321C & Hexachrome Black C.

1.Business Card Design
a. Logo
b. Name
c. Mobile
d. Landline
e. Website
f. Facebook
g. Twitter
2. Letterhead Design
a. Logo
b. Mobile
c. Landline
d. Website
e. CC reg number
f. BEE level 4 contributor
g. PRTVA member
h. Postal Address
3. Email Signature Design
a. Logo
b. Name
c. Mobile
d. Landline
e. BEE level 4 contributor
f. PRTVA member
g. Website
h. Facebook
i. Twitter
4. “Advertise Here” Design (for placement on empty billboards, etc) Majority ratio of 2:1 (eg 6m wide by 3m high) - Please use 2 attached photos.
a. Logo .co.za
b. Contact Mirela
c. Mobile
Nice to have
• Come up with a cool slogan / tagline for Business Cards, “Advertise Here” Design

```html
<!DOCTYPE html>
<html lang="en">
<head>
<meta charset="utf-8">
<title>Pin Oak Media – Business Card</title>
<link rel="stylesheet" href="https://fonts.googleapis.com/css2?family=Open+Sans:wght@400;600;700&display=swap">
<style>
  :root {
    --teal-dark: #008c95;
    --teal: #00a3ad;
    --teal-light: #6fccd3;
    --ink: #231f20;
    --grey: #5a5a5a;
    --grey-soft: #9a9a9a;
    --card: #ffffff;
    --backdrop: #ecebe8;
    --rule: #c9c9c9;
  }
  * { box-sizing: border-box; margin: 0; padding: 0; }
  html, body { width: 1200px; height: 466px; overflow: hidden; }
  body {
    background: var(--backdrop);
    font-family: "Open Sans", Arial, sans-serif;
    position: relative;
  }
  .card {
    position: absolute;
    top: 78px;
    width: 541px;
    height: 302px;
    background: var(--card);
    border-radius: 14px;
  }
  .card--front { left: 45px; }
  .card--back { left: 614px; }

  .brand {
    position: absolute;
    left: 40px;
    top: 148px;
    width: 250px;
    text-align: center;
  }
  .brand__name {
    font-size: 30px;
    font-weight: 700;
    color: var(--teal-dark);
    letter-spacing: -0.5px;
    line-height: 1;
  }
  .brand__tagline {
    margin-top: 10px;
    font-size: 12px;
    font-weight: 600;
    color: var(--grey-soft);
    letter-spacing: 1px;
  }

  .divider {
    position: absolute;
    left: 303px;
    top: 60px;
    width: 1px;
    height: 172px;
    background: linear-gradient(var(--rule), var(--rule) 70%, rgba(201,201,201,0));
  }

  .person {
    position: absolute;
    left: 323px;
    top: 58px;
  }
  .person__name {
    font-size: 17px;
    font-weight: 700;
    color: var(--teal-dark);
    line-height: 1.2;
  }
  .person__title {
    font-size: 13px;
    color: var(--grey);
  }

  .contacts {
    position: absolute;
    left: 323px;
    top: 124px;
    list-style: none;
  }
  .contacts li {
    display: flex;
    align-items: center;
    gap: 4px;
    height: 18px;
    font-size: 13px;
    color: var(--grey);
  }
  .contacts svg { width: 11px; height: 11px; flex: none; }

  .back-mark {
    position: absolute;
    left: 0;
    width: 100%;
    top: 104px;
    display: flex;
    justify-content: center;
    align-items: center;
    gap: 12px;
  }
  .back-mark__square {
    width: 26px;
    height: 26px;
    background: var(--teal);
  }
  .back-mark__name {
    font-size: 32px;
    font-weight: 700;
    color: var(--teal-dark);
    letter-spacing: -0.5px;
  }
  .back-url {
    position: absolute;
    left: 0;
    width: 100%;
    top: 196px;
    text-align: center;
    font-size: 13px;
    color: var(--grey);
    letter-spacing: 3px;
  }
</style>
</head>
<body>
  <section class="card card--front">
    <div class="brand">
      <div class="brand__name">Pin Oak Media</div>
      <div class="brand__tagline">Advertise Here</div>
    </div>

    <div class="divider"></div>

    <div class="person">
      <div class="person__name">Your Name</div>
      <div class="person__title">Title</div>
    </div>

    <ul class="contacts">
      <li>
        <svg viewBox="0 0 12 12" aria-hidden="true"><circle cx="6" cy="6" r="5.3" fill="none" stroke="#5a5a5a" stroke-width="1"/><path d="M4 3.5c.5 2 1.7 3.8 4 4.8l.6-1" fill="none" stroke="#5a5a5a" stroke-width="1.1"/></svg>
        +27 12345 67890
      </li>
      <li>
        <svg viewBox="0 0 12 12" aria-hidden="true"><rect x="3" y="1" width="6" height="10" rx="1" fill="none" stroke="#5a5a5a" stroke-width="1.1"/><rect x="4.2" y="2.4" width="3.6" height="4.6" fill="#5a5a5a"/></svg>
        +27 12345 67890
      </li>
      <li>
        <svg viewBox="0 0 12 12" aria-hidden="true"><circle cx="6" cy="6" r="5" fill="none" stroke="#5a5a5a" stroke-width="1"/><ellipse cx="6" cy="6" rx="2.2" ry="5" fill="none" stroke="#5a5a5a" stroke-width="0.8"/><line x1="1" y1="6" x2="11" y2="6" stroke="#5a5a5a" stroke-width="0.8"/></svg>
        www.pinoakmedia.com
      </li>
      <li>
        <svg viewBox="0 0 12 12" aria-hidden="true"><rect x="1" y="1" width="10" height="10" fill="#3b5b98"/></svg>
        pinoakmedia.com
      </li>
      <li>
        <svg viewBox="0 0 12 12" aria-hidden="true"><rect x="1" y="1" width="10" height="10" fill="#4fb6e6"/></svg>
        pinoakmedia.com
      </li>
    </ul>
  </section>

  <section class="card card--back">
    <div class="back-mark">
      <span class="back-mark__square"></span>
      <span class="back-mark__name">Pin Oak Media</span>
    </div>
    <div class="back-url">www.pinoakmedia.com</div>
  </section>
</body>
</html>
```